Design a calming beauty medical salon & spa website based in Hong Kong

We need help building an informational website for a beauty salon in Hong Kong. The local salon provides facials, massages, body and other slimming treatments in a relaxing environment. We offer some non-invasive medical treatments, such as botox. Having built the business on word of mouth, it is now time for us to launch a website to help market the business better. Website requirements:

-Must be responsive
-Use vibrant but clean colours. not too many, 1-2 colours
-Must be bilingual (switch between Chinese traditional and English)
-Our current website is host on a server, not using any particular platforms like wordpress

Pages:
1/ Homepage
2/ About us (incorporate gallery of salon photos and history of company)
3/ Promotions and latest deals (and leads them to sign up for more info, maybe pop-up small window when you click on a promotion)
4/ Treatment menus
4.1/Body treatments
4.2/ Face treatments
4.3/ Slimming treatments
5/ Showcasing products sold (no e-commerce functionality, just showing off products)
6/ Contact us (tel, address, map, opening hrs)

Footer - must haves include contact us info, privacy policy, terms & conditions, copyright blurb, join our company/employment page (with a form)

For information (comparable websites we like):
http://vostaria.com/
http://quimbel.com.hk/tc/aboutquimbel/background.php#centerenvi
Attaching a very first draft concept for this website
Attaching pictures of the beauty salon
Attaching logo

Target Market(s)

Hong Kong based, Chinese, females, 30-50+ age. 90% female clients.

Industry/Entity Type

Beauty Salon

Number of Pages Required

5+ page

Font styles to use
Sans Serif

Colors
f9d9e8
fbd3d4
fee3d5
fbe7d2
fee18a
fbf289
ffffff

Requirements
Must have
• interactive elements on website, such as scrolling banner photo headers
• incorporate photos of website salon
• connect to facebook page

```html
<!DOCTYPE html>
<html lang="en">
<head>
<meta charset="utf-8">
<title>Lumera Beauty</title>
<link rel="stylesheet" href="https://fonts.googleapis.com/css2?family=Open+Sans:wght@400;600&display=swap">
<style>
  :root {
    --plum: #5b2b72;
    --plum-soft: #6e3a84;
    --rose-icon: #b97c87;
    --blush: #fde9e0;
    --sand: #f4e6dc;
    --white: #ffffff;
    --ink: #2f2f2f;
    --footer: #2d2a2b;
    --hero-a: #8a5a60;
    --hero-b: #c99a9c;
    --hero-c: #e8c8c3;
    --room-a: #d9b3ad;
    --room-b: #ead1cb;
  }
  * { box-sizing: border-box; margin: 0; padding: 0; }
  html, body { width: 1200px; height: 2844px; overflow: hidden; }
  body { font-family: "Open Sans", sans-serif; color: var(--ink); background: var(--white); position: relative; }

  .site-header { position: absolute; top: 0; left: 0; width: 1200px; height: 104px; background: var(--white); }
  .brand { position: absolute; left: 84px; top: 24px; display: flex; align-items: center; gap: 12px; color: var(--plum); font-size: 30px; font-weight: 600; }
  .brand-dot { width: 38px; height: 38px; border-radius: 50%; background: var(--plum); }
  .main-nav { position: absolute; left: 427px; top: 52px; display: flex; gap: 35px; font-size: 17px; color: #4a4a4a; text-transform: uppercase; }
  .main-nav a { color: inherit; text-decoration: none; }
  .main-nav a.is-active { color: var(--plum); }

  .hero { position: absolute; top: 104px; left: 0; width: 1200px; height: 600px; background: linear-gradient(90deg, var(--hero-a) 0%, var(--hero-b) 50%, var(--hero-c) 100%); }
  .hero-title { position: absolute; left: 84px; top: 158px; width: 600px; color: var(--white); font-size: 38px; font-weight: 600; line-height: 46px; }
  .btn-outline-light { position: absolute; left: 84px; top: 363px; width: 209px; height: 69px; border: 3px solid var(--white); color: var(--white); font-size: 24px; display: flex; align-items: center; justify-content: center; }
  .slider-dots { position: absolute; top: 558px; left: 573px; display: flex; gap: 14px; }
  .slider-dots span { width: 15px; height: 15px; border-radius: 50%; border: 2px solid var(--white); }
  .slider-dots span.is-current { background: var(--white); }

  .section-title { color: var(--plum); font-weight: 600; text-transform: uppercase; }
  .btn-outline { border: 3px solid var(--plum); color: var(--plum); display: flex; align-items: center; justify-content: center; text-transform: uppercase; background: transparent; }

  .about { position: absolute; top: 704px; left: 0; width: 1200px; height: 345px; }
  .about .section-title { position: absolute; left: 84px; top: 36px; font-size: 33px; }
  .about-text { position: absolute; left: 84px; top: 90px; width: 990px; font-size: 21px; line-height: 40px; }
  .about .btn-outline { position: absolute; left: 84px; top: 238px; width: 189px; height: 57px; font-size: 23px; }

  .deals { position: absolute; top: 1049px; left: 0; width: 1200px; height: 600px; display: flex; }
  .deal { position: relative; width: 607px; height: 600px; background: var(--blush); }
  .deal + .deal { width: 593px; background: var(--sand); }
  .deal .section-title { position: absolute; left: 84px; top: 28px; font-size: 24px; font-weight: 400; }
  .deal + .deal .section-title, .deal + .deal .deal-photo, .deal + .deal .deal-text, .deal + .deal .price-tag { left: 69px; }
  .deal-photo { position: absolute; left: 84px; top: 87px; width: 458px; height: 297px; }
  .deal-photo.face { background: linear-gradient(90deg, #f1f1f1 0%, #f6e6dd 55%, #8fc9ec 100%); }
  .deal-photo.hair { width: 435px; background: linear-gradient(120deg, #3a3a48 0%, #8d776c 45%, #c8b7a8 70%, #2b3b6b 100%); }
  .deal-text { position: absolute; left: 84px; top: 418px; width: 420px; font-size: 19px; line-height: 28px; }
  .price-tag { position: absolute; left: 84px; top: 502px; width: 156px; height: 42px; border: 2px solid var(--plum); color: var(--plum); font-size: 22px; display: flex; align-items: center; justify-content: center; }

  .products { position: absolute; top: 1649px; left: 0; width: 1200px; height: 407px; }
  .product { position: absolute; top: 40px; width: 300px; }
  .product-icon { width: 74px; height: 74px; display: block; }
  .product .section-title { margin-top: 38px; font-size: 22px; font-weight: 400; }
  .product-text { margin-top: 28px; font-size: 19px; line-height: 27px; }
  .product .btn-outline { margin-top: 36px; width: 155px; height: 44px; border-width: 2px; font-size: 20px; }

  .contact { position: absolute; top: 2056px; left: 0; width: 1200px; height: 724px; background: linear-gradient(100deg, var(--room-a) 0%, var(--room-b) 45%, var(--room-a) 100%); }
  .contact .section-title { position: absolute; left: 84px; top: 36px; font-size: 35px; }
  .field-label { position: absolute; color: var(--plum); font-size: 25px; text-transform: uppercase; }
  .field-box { position: absolute; border: 3px solid var(--white); border-radius: 3px; }
  .contact .btn-outline { position: absolute; left: 84px; top: 626px; width: 232px; height: 54px; font-size: 25px; }

  .site-footer { position: absolute; top: 2780px; left: 0; width: 1200px; height: 64px; background: var(--footer); color: #eeeeee; font-size: 21px; display: flex; align-items: center; justify-content: center; }
</style>
</head>
<body>
  <header class="site-header">
    <div class="brand"><span class="brand-dot"></span>Lumera Beauty</div>
    <nav class="main-nav">
      <a class="is-active" href="#">Home</a>
      <a href="#">About</a>
      <a href="#">Latest Deals</a>
      <a href="#">Treatments</a>
      <a href="#">Products</a>
      <a href="#">Contact</a>
    </nav>
  </header>

  <section class="hero" role="img" aria-label="Banner photo of a woman applying red lipstick against a soft pink wall">
    <h1 class="hero-title">LUMERA BEAUTY : A unique solution for facials, massage, medical treatments.</h1>
    <a class="btn-outline-light">CONTACT NOW</a>
    <div class="slider-dots"><span class="is-current"></span><span></span><span></span></div>
  </section>

  <section class="about">
    <h2 class="section-title">About Us</h2>
    <p class="about-text">Lorem Ipsum is simply dummy text of the printing and typesetting industry. Lorem Ipsum has been the industry's standard dummy text ever since the 1500s, when an unknown printer took a galley of type and scrambled it to make a type specimen book.</p>
    <a class="btn-outline">Know More</a>
  </section>

  <section class="deals">
    <article class="deal">
      <h3 class="section-title">Latest Deals</h3>
      <div class="deal-photo face" role="img" aria-label="Photo of a facial injection treatment by a gloved practitioner"></div>
      <p class="deal-text">Lorem Ipsum is simply dummy text of the printing and typesetting industry.</p>
      <div class="price-tag">$56.10</div>
    </article>
    <article class="deal">
      <h3 class="section-title">Latest Deals</h3>
      <div class="deal-photo hair" role="img" aria-label="Photo of a woman examining a strand of her hair"></div>
      <p class="deal-text">Lorem Ipsum is simply dummy text of the printing and typesetting industry.</p>
      <div class="price-tag">$56.10</div>
    </article>
  </section>

  <section class="products">
    <article class="product" style="left:84px">
      <svg class="product-icon" viewBox="0 0 74 74" aria-hidden="true">
        <rect x="6" y="8" width="44" height="28" rx="12" fill="var(--rose-icon)"/>
        <rect x="50" y="14" width="14" height="16" rx="3" fill="var(--rose-icon)"/>
        <rect x="18" y="34" width="14" height="34" rx="4" fill="var(--rose-icon)"/>
      </svg>
      <h3 class="section-title">Our Products</h3>
      <p class="product-text">Morbi interdum mollis sapien. Sed ac risus. Phasellus lacinia, magna lorem ullamcorper.</p>
      <a class="btn-outline">Know More</a>
    </article>
    <article class="product" style="left:467px">
      <svg class="product-icon" viewBox="0 0 74 74" aria-hidden="true">
        <circle cx="42" cy="28" r="17" fill="none" stroke="var(--rose-icon)" stroke-width="5"/>
        <line x1="30" y1="40" x2="12" y2="64" stroke="var(--rose-icon)" stroke-width="7" stroke-linecap="round"/>
        <circle cx="12" cy="14" r="3" fill="var(--rose-icon)"/>
        <circle cx="66" cy="58" r="3" fill="var(--rose-icon)"/>
      </svg>
      <h3 class="section-title">Our Products</h3>
      <p class="product-text">Morbi interdum mollis sapien. Sed ac risus. Phasellus lacinia, magna lorem ullamcorper.</p>
      <a class="btn-outline">Know More</a>
    </article>
    <article class="product" style="left:833px">
      <svg class="product-icon" viewBox="0 0 74 74" aria-hidden="true">
        <rect x="18" y="4" width="16" height="10" rx="2" fill="var(--rose-icon)"/>
        <rect x="10" y="16" width="32" height="52" rx="6" fill="var(--rose-icon)"/>
        <path d="M46 66 C46 50 54 40 66 36 C68 52 60 62 46 66 Z" fill="var(--rose-icon)"/>
      </svg>
      <h3 class="section-title">Our Products</h3>
      <p class="product-text">Morbi interdum mollis sapien. Sed ac risus. Phasellus lacinia, magna lorem ullamcorper.</p>
      <a class="btn-outline">Know More</a>
    </article>
  </section>

  <section class="contact" role="img" aria-label="Softly tinted photo of the salon consultation room">
    <h2 class="section-title">Get in Touch</h2>
    <span class="field-label" style="left:84px;top:110px">Name</span>
    <span class="field-label" style="left:684px;top:110px">Email</span>
    <div class="field-box" style="left:84px;top:171px;width:487px;height:71px"></div>
    <div class="field-box" style="left:627px;top:171px;width:484px;height:71px"></div>
    <span class="field-label" style="left:84px;top:276px">Message</span>
    <div class="field-box" style="left:84px;top:340px;width:1027px;height:235px"></div>
    <a class="btn-outline">Send Message</a>
  </section>

  <footer class="site-footer">@2018. All Rights Reserved</footer>
</body>
</html>
```